a Label for a candle jar and its gift box

I would like a label that is modern minimalist for candles jars. These jars are colored as white, amber and black. I am thinking maybe foiling gold/silver background with logo only and maybe company name in different color that suits the foiling background color/s. I would like a high quality luxurious design that shows the preciousness of this candle. I am open to any ideas you might have for the design but so far I have used a logo only on the jar which I really like BUT I still feel that it is not enough branding for people when you only show them the logo so I am considering adding the business name. Again, I am open to both ideas (with logo only or logo with business name (Silken Meadow).

IMPORTANT: YOU MAY IGNORE MY DESIGN COMPLETELY AND DO YOUR OWN ONE AS LONG AS YOU KERP THE LOGO DESIGN. YOU MAY ALSO ADJUST THE LOGO A BIT TO SUIT YOUR DESIGN. - sorry im using capital letters to show importance but im not yelling :)

UPDATE: To clarify, I have uploaded a video called Corvel in the box to show what the current product look like. It is a corvel jar with a logo only and the jar box has a window that shows the jar with the logo on it and the back of that jar box has a bigger version of the label that has more details (i.e. Fragrance name and website link). So to make it clear, I would like to have two versions of the lables: 1. on the jar with minimal info (logo only or logo with the business name) 2. Bigger version of the label with more info to put on the back of the jar box - as described above. The dimensions of the jars are as per this link https://www.lunaxo-example.com.au/corvel-medium-base-and-flat-lid-amber-packed-with-lid-on/ The dimensions of the jar box as per this link https://www.lunaxo-example.com.au/corvel-medium-flat-lid-candle-box-with-window-beige/ Looking forward to some artistic productions :)

Update #2: Tues 25 Dec 18 1. I have uploaded the photo which has the logo with the name 'Silken Meadow' below it just for a reference. However, I would like the designer to modify the current font and NOT to use it as the word 'of in the phrase 'Silken Meadow' does not come out clear enough after printing. 2. I would like the designer NOT to create a design that will require a clear sticker/label for printing. 3. I have attached the photos of my current designs on the jars or the jar box just as a reference but please do NOT just use the same fonts and only change background. I am hoping to see something different and more professional than my own design :) Thank you very much!

Font styles to use
Decorative
Script

Requirements
Must have
• I would like them to fit on the three colors of the jars below - white, amber and black. Below is a link to how the jar looks like https://www.lunaxo-example.com.au/candle-making-supplies/candle-jars/corvel-candle-jars/?glassware_colour=415,443,417&glassware_size=268
Nice to have
• I would like to have a modern design which is suitable for both feminine and musculine.
Should not have
• shouldnt have so much writing on it!

```html
<!DOCTYPE html>
<html lang="en">
<head>
<meta charset="utf-8">
<title>Silken Meadow — Jar Label and Box Back Label</title>
<link rel="stylesheet" href="https://fonts.googleapis.com/css2?family=Cinzel:wght@400;600&family=Libre+Baskerville&family=Montserrat:wght@600&display=swap">
<style>
  :root {
    --canvas: #ffffff;
    --copper-light: #d6a577;
    --copper-mid: #b57a4c;
    --copper-deep: #7a4526;
    --ink: #1a0f08;
    --label-black: #000000;
    --label-edge: #2b2b2b;
    --copper-text: #c88a55;
  }
  html, body {
    margin: 0;
    padding: 0;
    width: 1200px;
    height: 950px;
    overflow: hidden;
    background: var(--canvas);
  }
  .sheet {
    position: relative;
    width: 1200px;
    height: 950px;
  }
  .jar-label {
    position: absolute;
    left: 250px;
    top: 140px;
    width: 300px;
    height: 600px;
  }
  .box-back-label {
    position: absolute;
    left: 640px;
    top: 190px;
    width: 330px;
    height: 470px;
    background: var(--label-edge);
    padding: 10px;
    box-sizing: border-box;
  }
  .box-back-label__inner {
    width: 100%;
    height: 100%;
    background: var(--label-black);
    border-radius: 8px;
    display: flex;
    flex-direction: column;
    align-items: center;
  }
  .brand-disc {
    margin-top: 34px;
    width: 260px;
    height: 260px;
    border-radius: 50%;
    background: linear-gradient(135deg, var(--copper-deep) 0%, var(--copper-light) 45%, var(--copper-mid) 70%, var(--copper-deep) 100%);
    display: flex;
    flex-direction: column;
    align-items: center;
    justify-content: center;
  }
  .brand-disc__name {
    font-family: "Cinzel", serif;
    font-weight: 600;
    font-size: 34px;
    line-height: 1.05;
    color: var(--ink);
    text-align: center;
    margin: 0;
  }
  .brand-disc__web {
    font-family: "Montserrat", sans-serif;
    font-weight: 600;
    font-size: 9px;
    color: var(--ink);
    margin-top: 16px;
  }
  .fragrance-name {
    font-family: "Libre Baskerville", serif;
    font-weight: 400;
    font-size: 23px;
    color: var(--copper-text);
    letter-spacing: 0.5px;
    margin: 26px 0 8px;
  }
  .fragrance-notes {
    font-family: "Libre Baskerville", serif;
    font-size: 9.5px;
    line-height: 1.3;
    color: var(--copper-text);
    text-align: center;
    margin: 0;
    width: 190px;
  }
</style>
</head>
<body>
<main class="sheet">
  <svg class="jar-label" viewBox="0 0 300 600" aria-label="Silken Meadow jar label">
    <defs>
      <linearGradient id="copperFoil" gradientUnits="userSpaceOnUse" x1="30" y1="0" x2="270" y2="600">
        <stop offset="0" stop-color="#6e3a1f"/>
        <stop offset="0.3" stop-color="#c08a5c"/>
        <stop offset="0.55" stop-color="#d9a97c"/>
        <stop offset="0.8" stop-color="#b37649"/>
        <stop offset="1" stop-color="#d0a073"/>
      </linearGradient>
    </defs>
    <g class="jar-label__shape" fill="url(#copperFoil)">
      <circle cx="150" cy="125" r="118"/>
      <rect x="112" y="180" width="76" height="400" rx="10"/>
    </g>
    <text class="jar-label__disc-name" x="150" y="118" text-anchor="middle"
          font-family="Cinzel, serif" font-weight="600" font-size="30" fill="#1a0f08">Silken</text>
    <text class="jar-label__disc-name" x="150" y="152" text-anchor="middle"
          font-family="Cinzel, serif" font-weight="600" font-size="30" fill="#1a0f08">Meadow</text>
    <text class="jar-label__tab-name" transform="translate(160 560) rotate(-90)"
          font-family="Cinzel, serif" font-weight="600" font-size="28" fill="#1a0f08">Silken Meadow</text>
  </svg>

  <section class="box-back-label" aria-label="Box back label">
    <div class="box-back-label__inner">
      <div class="brand-disc">
        <p class="brand-disc__name">Silken<br>Meadow</p>
        <span class="brand-disc__web">silkenmeadow-example.com.au</span>
      </div>
      <h2 class="fragrance-name">AMBER FIG</h2>
      <p class="fragrance-notes">A warm ode to the fig tree, softened by dark amber and cedar with bergamot, vanilla &amp; a hint of musk.</p>
    </div>
  </section>
</main>
</body>
</html>
```